Local Directory Ad

We currently have an advertisement in our local directory (see attached). We would like to make it look more appealing.
Dimensions are 110mm H X 175mm W
We would like to keep the same colours and contact details remain the same.
Most of the content can remain the same, Just remove the line Tax effective remote area salary packaging and add in Self Managed Super Funds.We want to change mortgage broking to Mortgage Broking and Loan Structuring.

We want to change the line Local accountants Local Knowledge Local Experience - to something like local knowledge beyond compare or unsurpassed local knowledge but open to suggestions on this.

there are some good designs posted so far. I particulalry like the ones from pulmawick, korbu41, and the last one posted by wexlorunti and PLV. Keep up the good work guys

```html
<!DOCTYPE html>
<html lang="en">
<head>
<meta charset="utf-8">
<title>Harbourline Accounting &amp; Finance – Directory Ad</title>
<link rel="stylesheet" href="https://fonts.googleapis.com/css2?family=Arimo:wght@700&family=Tenor+Sans&family=Oswald:wght@500&family=Tinos:wght@700&display=swap">
<style>
  :root {
    --ink: #000000;
    --navy: #2b2877;
    --blue: #1a6fbf;
    --frame: #2a2868;
    --white: #ffffff;
    --paper-grey: #e6e7e8;
    --paper-cream: #f6f4c0;
    --red: #b31e1e;
    --web-red: #9b2626;
    --tick-light: #6f9fd8;
    --tick-dark: #2d5ea8;
  }
  * { margin: 0; padding: 0; box-sizing: border-box; }
  html, body { width: 1200px; height: 756px; overflow: hidden; background: var(--ink); }
  .ad { position: relative; width: 1200px; height: 756px; background: var(--ink); font-family: "Arimo", Arial, sans-serif; }

  .tagline-band {
    position: absolute; left: 35px; top: 25px; width: 1130px; height: 79px;
    background: linear-gradient(90deg, var(--navy), var(--blue));
    display: flex; align-items: center; justify-content: center;
  }
  .tagline { color: var(--white); font-weight: 700; font-size: 41px; letter-spacing: 0.5px; margin-left: -60px; }

  .name-panel { position: absolute; left: 35px; top: 121px; width: 1130px; height: 165px; background: var(--white); }
  .name-frame {
    position: absolute; left: 14px; top: 15px; width: 1101px; height: 133px;
    border: 6px solid var(--frame);
  }
  .firm-name {
    position: absolute; left: 0; right: 0; top: 12px; text-align: center;
    font-family: "Tenor Sans", "Optima", sans-serif; font-size: 53px; color: var(--ink);
  }
  .licence {
    position: absolute; left: 278px; top: 82px;
    font-weight: 700; font-size: 27px; color: var(--frame); letter-spacing: 1.2px; white-space: nowrap;
  }

  .services-panel { position: absolute; left: 35px; top: 313px; width: 1130px; height: 394px; }
  .panel-shape { position: absolute; left: 0; top: 0; }
  .services-heading {
    position: absolute; left: 40px; top: 31px; white-space: nowrap;
    font-weight: 700; font-size: 41px; color: var(--red); letter-spacing: 1px;
  }
  .service-list { position: absolute; left: 22px; top: 98px; list-style: none; }
  .service-list li {
    display: flex; align-items: center; height: 42.6px; white-space: nowrap;
    font-family: "Oswald", "Arial Narrow", sans-serif; font-weight: 500; font-size: 31px; letter-spacing: 0.6px; color: var(--ink);
  }
  .tick { width: 36px; height: 30px; margin-right: 9px; flex: none; }

  .contact-box {
    position: absolute; left: 761px; top: 442px; width: 404px; height: 216px;
    background: linear-gradient(90deg, var(--navy), var(--blue));
    color: var(--white); font-weight: 700; font-size: 21px; letter-spacing: 0.8px; text-align: center;
    padding-top: 14px; line-height: 31.6px; white-space: nowrap;
  }

  .web {
    position: absolute; left: 761px; width: 404px; top: 672px; text-align: center;
    font-family: "Tinos", "Times New Roman", serif; font-weight: 700; font-size: 35px; color: var(--web-red); letter-spacing: 1.5px;
  }
</style>
</head>
<body>
<div class="ad">
  <div class="tagline-band"><span class="tagline">Unsurpassed local knowledge</span></div>

  <div class="name-panel">
    <div class="name-frame">
      <div class="firm-name">Harbourline Accounting &amp; Finance</div>
      <div class="licence">Australian Credit Licence 512 804</div>
    </div>
  </div>

  <div class="services-panel">
    <svg class="panel-shape" width="1130" height="394" viewBox="0 0 1130 394" aria-hidden="true">
      <defs>
        <linearGradient id="paper" x1="0" y1="0" x2="1" y2="0">
          <stop offset="0" stop-color="#e6e7e8"/>
          <stop offset="1" stop-color="#f6f4c0"/>
        </linearGradient>
      </defs>
      <path d="M0 0 H1130 V99 H693 V394 H0 Z" fill="url(#paper)"/>
    </svg>
    <div class="services-heading">We are here for you all year round to assist with...</div>
    <ul class="service-list">
      <li><svg class="tick" viewBox="0 0 36 30" aria-hidden="true"><path d="M2 14 L10 10 L16 18 L32 2 L35 6 L16 28 Z" fill="#2d5ea8"/><path d="M4 14 L10 12 L16 20 L32 4 L33 7 L16 25 Z" fill="#6f9fd8"/></svg>Accounting &amp; Taxation</li>
      <li><svg class="tick" viewBox="0 0 36 30" aria-hidden="true"><path d="M2 14 L10 10 L16 18 L32 2 L35 6 L16 28 Z" fill="#2d5ea8"/><path d="M4 14 L10 12 L16 20 L32 4 L33 7 L16 25 Z" fill="#6f9fd8"/></svg>Business Advise</li>
      <li><svg class="tick" viewBox="0 0 36 30" aria-hidden="true"><path d="M2 14 L10 10 L16 18 L32 2 L35 6 L16 28 Z" fill="#2d5ea8"/><path d="M4 14 L10 12 L16 20 L32 4 L33 7 L16 25 Z" fill="#6f9fd8"/></svg>CST and BAS’s</li>
      <li><svg class="tick" viewBox="0 0 36 30" aria-hidden="true"><path d="M2 14 L10 10 L16 18 L32 2 L35 6 L16 28 Z" fill="#2d5ea8"/><path d="M4 14 L10 12 L16 20 L32 4 L33 7 L16 25 Z" fill="#6f9fd8"/></svg>Mortgage Broking and Loan Structuring</li>
      <li><svg class="tick" viewBox="0 0 36 30" aria-hidden="true"><path d="M2 14 L10 10 L16 18 L32 2 L35 6 L16 28 Z" fill="#2d5ea8"/><path d="M4 14 L10 12 L16 20 L32 4 L33 7 L16 25 Z" fill="#6f9fd8"/></svg>Bookkeeping</li>
      <li><svg class="tick" viewBox="0 0 36 30" aria-hidden="true"><path d="M2 14 L10 10 L16 18 L32 2 L35 6 L16 28 Z" fill="#2d5ea8"/><path d="M4 14 L10 12 L16 20 L32 4 L33 7 L16 25 Z" fill="#6f9fd8"/></svg>Seff Managed Super Funds for your employes</li>
    </ul>
  </div>

  <div class="contact-box">
    <p>Shop 3 Marina Arcade</p>
    <p>12 Wattle St Saltport</p>
    <p>PO Box 418 Saltport 6799</p>
    <p>reception@hlnaf.com.au</p>
    <p>Ph: 9100 4827</p>
    <p>Fax: 9100 4828</p>
  </div>

  <div class="web">www.hlnaf.com.au</div>
</div>
</body>
</html>
```